Real Estate Development, Finance and Fund Management company

We need a business card and logo design for a new company based in Asia called 'Calloway Vance Ltd.'
We provide full service large scale real estate development services, including fund management, project delivery services and acquisitions. We are looking for a bold logo with a strong feeling of security. A good reference would be the Thornvale (www.thornvalehq.com) or Essenby Capital (www.essenbycap.com).
We will need to have the imagery for the cards and logos to be produced for a dark and light background, and for web and print quality.
Initial thoughts are to have silver text on a black or dark grey background but leave that to your discretion.
Final design should communicate stability, financial safety and building on a solid foundation.
NOTE : We are not looking for pictures or clip art. Logo should be primarily from text and anything additional should be limited and tasteful.
Thanks!

```html
<!DOCTYPE html>
<html lang="en">
<head>
<meta charset="utf-8">
<title>Calloway Vance Ltd. — Business Card</title>
<link href="https://fonts.googleapis.com/css2?family=Roboto:wght@400;500;700&family=Tinos:wght@700&display=swap" rel="stylesheet">
<style>
  :root {
    --page: #ffffff;
    --card-top: #23262b;
    --card-mid: #1b1e22;
    --card-low: #2a2e34;
    --header: #16181b;
    --bar: #070708;
    --rule: #8f959c;
    --silver: #b7bbc0;
    --text: #f2f3f5;
    --name: #a9a9a9;
  }
  * { margin: 0; padding: 0; box-sizing: border-box; }
  html, body { width: 1026px; height: 1200px; overflow: hidden; background: var(--page); }
  body { position: relative; font-family: "Roboto", Arial, sans-serif; }

  .card {
    position: absolute;
    left: 51px;
    width: 926px;
    height: 504px;
    border-radius: 24px;
    overflow: hidden;
    background: radial-gradient(ellipse at 50% 100%, var(--card-low) 0%, var(--card-mid) 60%, var(--card-top) 100%);
  }
  .card--front { top: 48px; }
  .card--back { top: 652px; height: 500px; }

  /* front header */
  .front-header {
    position: absolute; left: 0; top: 0; width: 100%; height: 124px;
    background: linear-gradient(#25282d, var(--header));
  }
  .front-header__rule {
    position: absolute; left: 346px; right: 0; top: 122px; height: 2px; background: var(--rule);
  }
  .front-header__bar {
    position: absolute; left: 0; top: 72px; width: 346px; height: 56px;
    background: var(--bar); border-top: 1px solid #3a3d42;
  }
  .brand {
    position: absolute; color: var(--silver); font-weight: 700; letter-spacing: -2px; white-space: nowrap;
  }
  .card--front .brand { right: 106px; top: 42px; font-size: 46px; line-height: 1; }

  .person { position: absolute; left: 84px; top: 312px; width: 300px; text-align: center; }
  .person__name {
    font-family: "Tinos", "Times New Roman", serif; font-weight: 700; font-size: 40px; color: var(--name);
    text-shadow: 0 3px 4px #000;
  }
  .person__role { font-weight: 700; font-size: 32px; color: var(--text); margin-top: 2px; }

  .contact { position: absolute; right: 128px; top: 0; text-align: right; color: var(--text); font-size: 29px; line-height: 35px; }
  .contact__line { position: absolute; right: 0; white-space: nowrap; }
  .icon { position: absolute; left: 842px; width: 32px; height: 32px; fill: var(--text); }

  /* back */
  .card--back .brand { left: 0; width: 100%; text-align: center; top: 170px; font-size: 64px; line-height: 1; letter-spacing: -3px; }
  .web { position: absolute; left: 0; width: 100%; text-align: center; top: 245px; font-size: 29px; color: var(--text); }
  .back-footer {
    position: absolute; left: 0; bottom: 0; width: 100%; height: 106px;
    background: linear-gradient(#141619, #202328);
  }
  .back-footer__rule { position: absolute; left: 0; width: 656px; top: 0; height: 2px; background: var(--rule); }
  .back-footer__bar {
    position: absolute; left: 656px; right: 0; top: -2px; height: 57px;
    background: var(--bar); border-bottom: 1px solid #3a3d42;
  }
</style>
</head>
<body>

<section class="card card--front">
  <div class="front-header">
    <div class="front-header__bar"></div>
    <div class="front-header__rule"></div>
  </div>
  <div class="brand">Calloway Vance Ltd.</div>

  <div class="person">
    <div class="person__name">Marcus Hale</div>
    <div class="person__role">Director</div>
  </div>

  <div class="contact" style="left:0;">
    <div class="contact__line" style="top:186px;">2207 Harbourline Rd,</div>
    <div class="contact__line" style="top:220px;">Eastvale North Province</div>
    <div class="contact__line" style="top:270px;">03 6420 8315</div>
    <div class="contact__line" style="top:322px;">03 6420 8315</div>
    <div class="contact__line" style="top:374px;">0427 903 618</div>
    <div class="contact__line" style="top:418px;">office@callowayvance.com</div>
  </div>

  <svg class="icon" style="top:208px;" viewBox="0 0 32 32" aria-hidden="true"><path d="M16 4 3 15h4v12h7v-8h4v8h7V15h4z"/></svg>
  <svg class="icon" style="top:273px;" viewBox="0 0 32 32" aria-hidden="true"><path d="M3 12c0-4 6-6 13-6s13 2 13 6v2h-7v-3h-12v3H3z"/><path d="M8 17l4-5h8l4 5v9H8z"/><circle cx="16" cy="20" r="3" fill="#1d2024"/></svg>
  <svg class="icon" style="top:323px;" viewBox="0 0 32 32" aria-hidden="true"><path d="M9 3h14v9H9z" fill="none" stroke="#f2f3f5" stroke-width="2"/><path d="M12 6h8M12 9h8" stroke="#f2f3f5" stroke-width="1.5"/><path d="M4 13h24v15H4z" fill="none" stroke="#f2f3f5" stroke-width="2"/><path d="M8 18h16v2H8zM8 23h16v2H8z"/></svg>
  <svg class="icon" style="top:373px;" viewBox="0 0 32 32" aria-hidden="true"><rect x="9" y="2" width="14" height="28" rx="2" fill="none" stroke="#f2f3f5" stroke-width="2"/><rect x="11" y="6" width="10" height="18"/><circle cx="16" cy="27" r="1.3"/></svg>
  <svg class="icon" style="top:422px;" viewBox="0 0 32 32" aria-hidden="true"><path d="M3 8h26v17H3z"/><path d="M3 8l13 10L29 8M3 25l10-9M29 25l-10-9" fill="none" stroke="#1d2024" stroke-width="2"/></svg>
</section>

<section class="card card--back">
  <div class="brand">Calloway Vance Ltd.</div>
  <div class="web">www.callowayvance.com</div>
  <div class="back-footer">
    <div class="back-footer__rule"></div>
    <div class="back-footer__bar"></div>
  </div>
</section>

</body>
</html>
```